Simple HVAC & Electrical Contractor Billboard

Leasing a 12'3" H by 49'3" W billboard. I'd like to use our current logo and add a few words to let people know what we do. Looking for a clean simple look.
Our company name is Harold Pruett Mechanical - What we are is Air Conditioning & Electrical Contractors.

Our license numbers are TACLA00052916K & TECL71420 they will need to be visible on the sign somewhere.

I'm not sure how much information I want to see on the sign. I want to keep it clean but some of our contact info is as follows. Office # 555-208-4619 - Webpage hpmexample.com. I feel like most people can search the name to find the contact info they need but I'll defer to the designers to come up with the best design.

I have attached a couple different logos we have used I the past.

```html
<!DOCTYPE html>
<html lang="en">
<head>
<meta charset="utf-8">
<title>Harold Pruett Mechanical – Billboard Concepts</title>
<link rel="stylesheet" href="https://fonts.googleapis.com/css2?family=Roboto+Condensed:wght@400;700&family=Montserrat:wght@500;600&family=Arimo:wght@700&display=swap">
<style>
  :root {
    --red: #ed1c24;
    --black: #000000;
    --white: #ffffff;
    --stage-light: #6a6a6b;
    --stage-dark: #2e2e30;
  }
  html, body {
    margin: 0;
    padding: 0;
    width: 1200px;
    height: 960px;
    overflow: hidden;
  }
  .canvas {
    position: relative;
    width: 1200px;
    height: 960px;
    background: var(--white);
    overflow: hidden;
  }
  .stage-dark {
    position: absolute;
    left: 0;
    top: 518px;
    width: 1200px;
    height: 442px;
    background: radial-gradient(ellipse at 50% 45%, var(--stage-light) 0%, #4e4e50 55%, var(--stage-dark) 100%);
  }
  .billboard {
    position: absolute;
    left: 48px;
    width: 1104px;
    height: 274px;
    overflow: hidden;
    font-family: "Roboto Condensed", "Arial Narrow", sans-serif;
  }
  .billboard--dark { top: 114px; background: var(--black); color: var(--white); }
  .billboard--light { top: 582px; background: var(--white); color: var(--black); }

  .kicker {
    position: absolute;
    left: 33px;
    top: 18px;
    margin: 0;
    font-weight: 700;
    font-size: 52px;
    line-height: 1;
    color: var(--red);
    white-space: nowrap;
    transform: scaleX(0.86);
    transform-origin: left;
  }
  .headline {
    position: absolute;
    left: 32px;
    top: 70px;
    margin: 0;
    font-weight: 700;
    font-size: 58px;
    line-height: 1;
    white-space: nowrap;
    transform: scaleX(0.89);
    transform-origin: left;
  }
  .sectors {
    position: absolute;
    left: 33px;
    top: 135px;
    margin: 0;
    font-weight: 700;
    font-size: 24px;
    line-height: 1;
    white-space: nowrap;
  }
  .phone-band {
    position: absolute;
    left: 0;
    top: 184px;
    width: 356px;
    height: 46px;
  }
  .phone-band svg { position: absolute; inset: 0; }
  .phone {
    position: absolute;
    left: 34px;
    top: 6px;
    margin: 0;
    font-weight: 700;
    font-size: 33px;
    line-height: 1;
    color: var(--white);
    white-space: nowrap;
  }
  .website {
    position: absolute;
    left: 34px;
    top: 234px;
    margin: 0;
    font-family: "Arimo", Arial, sans-serif;
    font-weight: 700;
    font-size: 24.4px;
    line-height: 1;
    white-space: nowrap;
  }
  .license-label {
    position: absolute;
    left: 398px;
    top: 221px;
    margin: 0;
    font-family: "Arimo", Arial, sans-serif;
    font-weight: 700;
    font-size: 13px;
    color: var(--red);
    line-height: 1;
  }
  .license-numbers {
    position: absolute;
    left: 398px;
    top: 241px;
    margin: 0;
    font-family: "Arimo", Arial, sans-serif;
    font-weight: 700;
    font-size: 13px;
    line-height: 1;
    white-space: nowrap;
  }
  .brand-card {
    position: absolute;
    left: 0;
    top: 0;
    width: 1104px;
    height: 274px;
  }
  .brand-mark {
    position: absolute;
    left: 850px;
    top: 62px;
    width: 82px;
    height: 82px;
    background: var(--red);
  }
  .brand-name {
    position: absolute;
    left: 718px;
    top: 168px;
    margin: 0;
    font-family: "Montserrat", Arial, sans-serif;
    font-weight: 600;
    font-size: 39px;
    line-height: 1;
    letter-spacing: -0.5px;
    white-space: nowrap;
  }
  .brand-tagline {
    position: absolute;
    left: 719px;
    top: 212px;
    margin: 0;
    font-family: "Montserrat", Arial, sans-serif;
    font-weight: 500;
    font-size: 16.8px;
    line-height: 1;
    color: var(--red);
    white-space: nowrap;
  }
  .billboard--dark .brand-name { color: var(--black); }
  .billboard--light .brand-name { color: var(--white); }
  .card-frame { fill: var(--red); }
  .billboard--dark .card-face { fill: var(--white); }
  .billboard--light .card-face { fill: var(--black); }
  .band-fill { fill: var(--red); }
</style>
</head>
<body>
<main class="canvas">
  <div class="stage-dark"></div>

  <section class="billboard billboard--dark" aria-label="Billboard, dark version">
    <h2 class="kicker">SPECIALIZING IN</h2>
    <h1 class="headline">SERVICE &amp; INSTALLATION</h1>
    <p class="sectors">Servicing Residential, Commercial and Industrial Sectors</p>
    <div class="phone-band">
      <svg viewBox="0 0 356 46" width="356" height="46"><polygon class="band-fill" points="0,0 344,0 356,46 0,46"/></svg>
      <p class="phone">Office # 555-208-4619</p>
    </div>
    <p class="website">website: hpmexample.com</p>
    <p class="license-label">license numbers</p>
    <p class="license-numbers">TACLA00052916K &amp; TECL71420</p>
    <svg class="brand-card" viewBox="0 0 1104 274" width="1104" height="274">
      <polygon class="card-frame" points="677,58 938,0 1080,0 1099,274 690,274"/>
      <polygon class="card-face" points="684,65 938,1 1066,1 1093,262 950,274 702,274"/>
    </svg>
    <div class="brand-mark"></div>
    <p class="brand-name">HAROLD PRUETT</p>
    <p class="brand-tagline">Air Conditioning &amp; Electrical Contractors</p>
  </section>

  <section class="billboard billboard--light" aria-label="Billboard, light version">
    <h2 class="kicker">SPECIALIZING IN</h2>
    <h1 class="headline">SERVICE &amp; INSTALLATION</h1>
    <p class="sectors">Servicing Residential, Commercial and Industrial Sectors</p>
    <div class="phone-band">
      <svg viewBox="0 0 356 46" width="356" height="46"><polygon class="band-fill" points="0,0 344,0 356,46 0,46"/></svg>
      <p class="phone">Office # 555-208-4619</p>
    </div>
    <p class="website">website: hpmexample.com</p>
    <p class="license-label">license numbers</p>
    <p class="license-numbers">TACLA00052916K &amp; TECL71420</p>
    <svg class="brand-card" viewBox="0 0 1104 274" width="1104" height="274">
      <polygon class="card-frame" points="677,58 938,0 1080,0 1099,274 690,274"/>
      <polygon class="card-face" points="684,65 938,1 1066,1 1093,262 950,274 702,274"/>
    </svg>
    <div class="brand-mark"></div>
    <p class="brand-name">HAROLD PRUETT</p>
    <p class="brand-tagline">Air Conditioning &amp; Electrical Contractors</p>
  </section>
</main>
</body>
</html>
```